Local Contractor needs Upscale Web Design

This website needs to have an upscale look with a very modern feel.

This is for a home page psd layout

Please build your psd file to match the look of this template: http://www.layoutquarry.example/demo/38162.html

Please change the color scheme to the colors of the attached logo

Add Logo that is attached.

Phone Number:
507-392-4186

Must Include these pages in a horizontal menu bar in this order:
Home, About, Services, Portfolio, Testimonials, Contact

For the rotating banners:
1. Construction - 35+ Years and Growing
2. Capabilities - Complete Line of Services
3. Commitment - Quality and Attention to Detail

Images under rotating banner:
Image 1, 2, 3 (Attached - Crop to fit)

What We're Thinking Section - Change title text to "Retail Space Construction" (Fill the remainder with latin text)

Who Are We Section - Change title text to "Industrial Construction" (Fill the remainder with latin text)

Project Gallery - Image 4, 5, 6, 7 (Attached - Crop to fit)

Remove the sections towards the bottom titled "Why Us" & "Services"

Please make the map show this address:
2917 86th St SW, Pine Hollow, MN 55104

Footer:
Ridgeway Bolt Construction © 2015 | Powered by Marlo Pixel Works

```html
<!DOCTYPE html>
<html lang="en">
<head>
<meta charset="utf-8">
<title>Ridgeway Bolt Construction</title>
<link href="https://fonts.googleapis.com/css2?family=Mulish:wght@400;600;700;800&display=swap" rel="stylesheet">
<style>
:root{
  --brand:#8b1a24;
  --brand-deep:#6e1219;
  --brand-soft:#a8404a;
  --ink:#2b2b2b;
  --muted:#9a9a9a;
  --nav:#8a8a8a;
  --rule:#e6e6e6;
  --pale:#f1f0f6;
  --white:#ffffff;
}
*{margin:0;padding:0;box-sizing:border-box}
html,body{width:1200px;height:2338px;overflow:hidden;background:var(--white)}
body{position:relative;font-family:"Mulish",sans-serif;color:var(--ink)}
.abs{position:absolute}

/* header */
.site-header{left:0;top:0;width:1200px;height:136px;background:var(--white)}
.brand-name{left:175px;top:62px;display:flex;align-items:center;gap:10px;font-size:20px;font-weight:800;color:var(--brand);letter-spacing:.5px;text-transform:uppercase}
.brand-name .mark{width:18px;height:18px;background:var(--brand)}
.phone{left:880px;top:18px;display:flex;align-items:center;gap:12px;font-size:18px;color:var(--nav)}
.main-nav{left:0;top:85px;width:1200px;font-size:17px;color:var(--nav)}
.main-nav a{position:absolute;text-decoration:none;color:inherit}
.main-nav a.active{color:var(--brand);font-weight:700;border-bottom:2px solid var(--brand);padding-bottom:4px}

/* hero */
.hero{left:0;top:136px;width:1200px;height:478px;background:linear-gradient(180deg,#b0505a 0%,#a23a45 45%,#9a3440 100%)}
.hero-title{left:182px;top:178px;font-size:62px;font-weight:700;color:var(--white);letter-spacing:1px}
.hero-sub{left:192px;top:254px;font-size:20px;color:var(--white);letter-spacing:.5px}
.hero-arrow{top:206px}
.dots{left:198px;top:443px;display:flex;gap:4px}
.dots span{width:14px;height:14px;border-radius:50%;border:2px solid var(--white)}
.dots span.on{background:var(--white)}

/* feature tiles */
.tile{background:#888}
.tile-main{left:177px;top:674px;width:550px;height:386px;background:linear-gradient(135deg,#9c3a44,#7e1e28)}
.tile-kitchen{left:732px;top:674px;width:291px;height:191px;background:linear-gradient(135deg,#e6e4e1,#a9a5a0)}
.tile-bath{left:732px;top:869px;width:291px;height:191px;background:linear-gradient(135deg,#8c8680,#3c3936)}
.view-more{left:177px;top:826px;width:550px;text-align:center;color:var(--white);font-size:20px;font-weight:700}
.view-more svg{display:block;margin:0 auto 4px}
.gallery-bar{left:177px;top:1066px;width:844px;height:35px;background:var(--brand);color:var(--white);font-size:16px;text-align:center;line-height:35px;letter-spacing:.5px}

/* intro columns */
.intro{top:1180px;width:396px}
.intro h2{font-size:24px;font-weight:800;color:var(--brand);padding-bottom:14px;border-bottom:1px solid var(--rule);text-transform:uppercase;letter-spacing:.3px}
.intro h3{font-size:23px;font-weight:400;margin-top:16px;color:#1e1e1e}
.intro p{font-size:13.5px;line-height:17px;color:#b3b3b3;margin-top:12px}
.read-more{left:173px;top:1369px;width:154px;height:49px;background:var(--brand);color:var(--white);font-size:16px;text-align:center;line-height:49px}

/* project gallery */
.section-title{left:171px;top:1530px;font-size:23px;font-weight:800;color:var(--brand);letter-spacing:.3px}
.section-rule{left:171px;top:1562px;width:857px;height:1px;background:var(--rule)}
.next-btn{left:939px;top:1525px;width:52px;height:37px;background:#e8e7f4}
.shot{width:425px;height:181px}
.shot-1{left:173px;top:1586px;background:linear-gradient(135deg,#6e4a2e,#c8b38d 60%,#3a2a1f)}
.shot-2{left:602px;top:1586px;width:426px;background:linear-gradient(135deg,#b89676,#5a534c 55%,#a8aea8)}
.shot-3{left:173px;top:1771px;background:linear-gradient(135deg,#d6d6d4,#8a8886);border:5px solid var(--brand)}
.shot-4{left:602px;top:1771px;width:426px;background:linear-gradient(135deg,#6a6460,#d9d7d2 60%,#8a8480)}

/* map */
.map{left:0;top:2032px;width:1200px;height:237px;background:linear-gradient(135deg,#ecebe6,#e3e6df)}
.map-address{left:504px;top:2145px;font-size:17px;line-height:21px;color:#222}
.map-pin{left:588px;top:2080px}
.zoom{left:24px;top:2040px}

/* footer */
.site-footer{left:0;top:2269px;width:1200px;height:69px;background:var(--pale)}
.footer-text{left:181px;top:2296px;font-size:13px;color:#8c8c9c}
.footer-text b{font-weight:700}
.to-top{left:871px;top:2269px;width:156px;height:69px;background:var(--brand)}
</style>
</head>
<body>

<header class="abs site-header">
  <div class="abs brand-name"><span class="mark"></span>Ridgeway Bolt Construction</div>
  <div class="abs phone">
    <svg width="16" height="28" viewBox="0 0 16 28"><rect x="1.5" y="1.5" width="13" height="25" rx="2" fill="none" stroke="#8b1a24" stroke-width="2"/><line x1="5" y1="22" x2="11" y2="22" stroke="#8b1a24" stroke-width="2"/></svg>
    <span>507-392-4186</span>
  </div>
  <nav class="abs main-nav">
    <a class="active" style="left:481px">Home</a>
    <a style="left:561px">About</a>
    <a style="left:647px">Services</a>
    <a style="left:740px">Portfolio</a>
    <a style="left:834px">Testimonials</a>
    <a style="left:953px">Contact</a>
  </nav>
</header>

<section class="abs hero" role="img" aria-label="Photo of a finished retail storefront under a deep red overlay"></section>
<div class="abs hero-title">CONSTRUCTION</div>
<div class="abs hero-sub">OF YOUR DREAMS</div>
<svg class="abs hero-arrow" style="left:8px" width="18" height="36" viewBox="0 0 18 36"><polyline points="15,2 3,18 15,34" fill="none" stroke="#fff" stroke-width="2.5"/></svg>
<svg class="abs hero-arrow" style="left:1172px" width="18" height="36" viewBox="0 0 18 36"><polyline points="3,2 15,18 3,34" fill="none" stroke="#fff" stroke-width="2.5"/></svg>
<div class="abs dots"><span class="on"></span><span></span><span></span></div>

<div class="abs tile tile-main" role="img" aria-label="Photo of a stone fireplace showroom under a red overlay"></div>
<div class="abs tile tile-kitchen" role="img" aria-label="Photo of a white kitchen with dark countertop"></div>
<div class="abs tile tile-bath" role="img" aria-label="Photo of a bathroom with freestanding tub"></div>
<div class="abs view-more">
  <svg width="28" height="28" viewBox="0 0 28 28"><circle cx="12" cy="12" r="8" fill="none" stroke="#fff" stroke-width="2"/><line x1="18" y1="18" x2="25" y2="25" stroke="#fff" stroke-width="2.5"/><line x1="8" y1="12" x2="16" y2="12" stroke="#fff" stroke-width="2"/><line x1="12" y1="8" x2="12" y2="16" stroke="#fff" stroke-width="2"/></svg>
  VIEW MORE
</div>
<div class="abs gallery-bar">VIEW GALLERY</div>

<article class="abs intro" style="left:171px">
  <h2>Retail Space Construction</h2>
  <h3>Lorem ipsum dolor sit amet</h3>
  <p>Lorem ipsum dolor sit amet, consectetuer adipiscing elit, sed diam nonummy nibh euismod tincidunt ut laoreet dolore magna aliquam erat volutpat.</p>
</article>
<article class="abs intro" style="left:653px">
  <h2>Industrial Construction</h2>
  <h3>Lorem ipsum dolor sit amet</h3>
  <p>Lorem ipsum dolor sit amet, consectetuer adipiscing elit, sed diam nonummy nibh euismod tincidunt ut laoreet dolore magna aliquam erat volutpat.</p>
</article>
<div class="abs read-more">READ MORE</div>

<h2 class="abs section-title">PROJECT GALLERY</h2>
<div class="abs next-btn">
  <svg width="52" height="37" viewBox="0 0 52 37"><polyline points="23,13 29,18.5 23,24" fill="none" stroke="#555" stroke-width="2"/></svg>
</div>
<div class="abs section-rule"></div>
<div class="abs shot shot-1" role="img" aria-label="Photo of a kitchen with dark wood cabinets"></div>
<div class="abs shot shot-2" role="img" aria-label="Photo of a stone accent wall and bathroom vanity"></div>
<div class="abs shot shot-3" role="img" aria-label="Photo of a white kitchen with black countertop"></div>
<div class="abs shot shot-4" role="img" aria-label="Photo of a bathroom with vessel sink and tub"></div>

<div class="abs map" role="img" aria-label="Street map centred on the office location"></div>
<svg class="abs zoom" width="44" height="150" viewBox="0 0 44 150"><circle cx="22" cy="20" r="18" fill="#f7f7f7" stroke="#ccc"/><rect x="12" y="80" width="20" height="20" fill="#fff" stroke="#ccc"/><rect x="12" y="110" width="20" height="20" fill="#fff" stroke="#ccc"/><line x1="17" y1="90" x2="27" y2="90" stroke="#666" stroke-width="2"/><line x1="22" y1="85" x2="22" y2="95" stroke="#666" stroke-width="2"/><line x1="17" y1="120" x2="27" y2="120" stroke="#666" stroke-width="2"/></svg>
<svg class="abs map-pin" width="36" height="52" viewBox="0 0 36 52"><path d="M18 2C9 2 2 9 2 18c0 12 16 32 16 32s16-20 16-32C34 9 27 2 18 2z" fill="#8b1a24"/><circle cx="18" cy="18" r="7" fill="#fff"/></svg>
<div class="abs map-address">2917 86th St SW, Pine<br>Hollow, MN 55104</div>

<footer class="abs site-footer"></footer>
<div class="abs footer-text"><b>Ridgeway Bolt Construction</b> © 2015 &nbsp;|&nbsp; Powered by <b>Marlo Pixel Works</b></div>
<div class="abs to-top">
  <svg width="156" height="69" viewBox="0 0 156 69"><polyline points="66,40 78,28 90,40" fill="none" stroke="#fff" stroke-width="2.5"/></svg>
</div>

</body>
</html>
```